Company Profile for Consulting Comany

Need Company profile to be designed in a professional way.

for inspiring :-
https://www.folivane.net/gallery/5372904/COMPANY-PROFILE
https://www.folivane.net/gallery/60391742/Biotech-Product-Catalog-No1-(Laminar-Air-Flow)
https://www.folivane.net/gallery/73905218/MPG-Globalpath-Company-Profile-2014-(MPG-Rebrand-part-2)

Target Market(s)

Corporate

Industry/Entity Type

It Company

Font styles to use
Sans Serif

Requirements
Must have
• Landscape A4 size
• Must go with the logo branding
• Must Have Visual Identity is the most important
• Must Have mpty spaces

```html
<!DOCTYPE html>
<html lang="en">
<head>
<meta charset="utf-8">
<title>Kestrel Advisory – Company Profile Board</title>
<link href="https://fonts.googleapis.com/css2?family=Open+Sans:wght@400;600;700&display=swap" rel="stylesheet">
<style>
:root{
  --board:#8a5a22;
  --ink:#111214;
  --black:#0b0c0e;
  --brand:#1fa3d8;
  --brand-deep:#2d8fd6;
  --sky:#4aa5e6;
  --heading:#1d6fae;
  --gray:#4a4d52;
  --bar:#c9dcf2;
  --white:#ffffff;
}
*{box-sizing:border-box;margin:0;padding:0}
html,body{width:1200px;height:907px;overflow:hidden;background:var(--board);font-family:"Open Sans",Arial,sans-serif}
.board{position:relative;width:1200px;height:907px}
.abs{position:absolute}
.label{position:absolute;transform:translateX(-50%);color:var(--white);font-weight:700;font-size:17px;white-space:nowrap}
.page{position:absolute;width:530px;overflow:hidden;box-shadow:2px 2px 4px rgba(0,0,0,.35)}

/* Brand name set as text */
.brand{display:flex;align-items:center;gap:4px;color:var(--brand);font-weight:600;white-space:nowrap}
.brand i{display:inline-block;background:var(--brand)}

/* Cover */
.cover{left:58px;top:69px;height:376px;background:var(--black)}
.forest{left:30px;top:19px;width:472px;height:280px;background:radial-gradient(ellipse at 50% 30%,#8d8d8d 0%,#4a4a4a 45%,#161616 85%)}
.cover-intro{left:0;width:100%;top:127px;text-align:center;color:#e6e6e6;font-size:11px}
.cover-title{left:0;width:100%;top:143px;text-align:center;color:var(--white);font-size:18.5px;font-weight:700}
.cover-pillars{left:0;width:100%;top:189px;text-align:center;color:var(--brand);font-size:7px}
.cover-badge{left:202px;top:249px;width:122px;height:127px;background:#000;border-radius:10px 10px 0 0;display:flex;align-items:center;justify-content:center}
.cover-badge .brand{flex-direction:column;font-size:15px;gap:6px;text-align:center;line-height:1.05}
.cover-badge .brand i{width:30px;height:30px}

/* Shared page footer */
.footer{left:0;width:530px;height:20px;background:var(--black);display:flex;align-items:center;padding:0 22px 0 24px;justify-content:space-between}
.footer .pillars{color:#e8e8e8;font-size:7.5px}
.footer .num{position:absolute;left:256px;top:2px;width:16px;height:16px;border-radius:50%;background:#e8e8e8;color:#111;font-size:7px;font-weight:700;display:flex;align-items:center;justify-content:center}
.footer .brand{font-size:11px}
.footer .brand i{width:7px;height:7px}

/* Page 3 */
.p3{left:602px;top:70px;height:372px;background:var(--white)}
.p3-blue{left:264px;top:0;width:266px;height:336px;background:linear-gradient(160deg,#3a99e0,#2b86d2 60%,#4aa2e3)}
.p3-wash{left:0;top:0;width:264px;height:336px;background:linear-gradient(170deg,#e3f0fa 0%,#ffffff 30%,#ffffff 80%,#eaf3fb 100%)}
.p3-title{left:24px;top:18px;font-size:18.5px;font-weight:700;color:var(--gray)}
.reason{left:20px;width:222px}
.reason h3{background:var(--bar);color:var(--heading);font-size:7.5px;font-weight:400;padding:0 3px;height:10px;line-height:10px}
.reason p{font-size:5.2px;line-height:8.6px;color:var(--gray);padding:3px 3px 0;text-align:justify}
.photo{width:114px;height:70px;border:2px solid #fff;background:linear-gradient(160deg,#dfe6ee,#9fb2c6 55%,#5d7390)}

/* Page 1 */
.p1{left:58px;top:460px;height:374px;background:var(--black)}
.toc{left:33px;top:15px;width:236px;height:343px;border-radius:8px;background:linear-gradient(135deg,#eef1f4,#d6dee6 45%,#c2ccd6 80%,#e1e5ea)}
.toc-title{left:9px;top:10px;color:#2f7bb8;font-size:16px;font-weight:600}
.toc-row{position:absolute;left:-33px;width:298px;display:flex;justify-content:space-between;font-size:6.4px;color:#2b2d30}
.toc-row.main{left:-12px;width:278px;height:13px;line-height:13px;background:var(--white);border-radius:7px 0 0 7px;color:#2f7bb8;padding:0 10px 0 12px;box-shadow:0 1px 1px rgba(0,0,0,.25)}
.toc-row.sub{left:16px;width:234px;padding-right:2px}
.p1-brand{left:306px;top:172px}
.p1-brand .brand{font-size:17px}
.p1-brand .brand i{width:13px;height:13px}
.p1-rule{left:306px;top:195px;width:170px;height:1px;background:#2a2f36}

/* Page 2 */
.p2{left:602px;top:461px;height:373px;background:linear-gradient(165deg,#eaf4fb 0%,#ffffff 35%,#e6f1fa 70%,#cfe4f6 100%)}
.p2-band{left:0;top:13px;width:530px;height:30px;background:linear-gradient(90deg,#3d9be0,#5aade7)}
.p2-title{left:24px;top:17px;color:var(--white);font-size:18.5px;font-weight:700}
.h{color:var(--heading);font-size:9px;font-weight:600}
.copy{font-size:5.3px;line-height:8.8px;color:#2b2d30;text-align:justify}
.mission-list{list-style:none}
.mission-list li{position:relative;padding-left:10px;font-size:5.3px;line-height:8.8px;color:#2b2d30;margin-bottom:2.5px}
.mission-list li::before{content:"";position:absolute;left:0;top:2px;width:6px;height:6px;border-radius:50%;background:var(--brand-deep)}
.values{left:22px;top:196px;width:483px}
.values-head{display:flex;height:17px;background:var(--black);color:var(--white);font-size:9px;font-weight:600;line-height:17px}
.values-head span:first-child{width:122px;padding-left:8px;border-right:1px solid #555}
.values-row{display:flex;height:12px;line-height:12px;font-size:5.2px;color:var(--white);border-bottom:1px solid rgba(255,255,255,.55)}
.values-row .k{width:122px;background:#3a90d7;font-weight:700;padding-left:8px;display:flex;align-items:center;gap:4px}
.values-row .v{flex:1;background:#4ba0e2;padding-left:8px}
.values-row svg{width:7px;height:7px}
</style>
</head>
<body>
<div class="board">

  <div class="label" style="left:298px;top:38px">Front Cover</div>
  <div class="label" style="left:886px;top:40px">Page 3 (Inside page)</div>
  <div class="label" style="left:338px;top:842px">Page 1 (Content page)</div>
  <div class="label" style="left:887px;top:840px">Page 2 (Inside page)</div>

  <!-- Front cover -->
  <section class="page cover">
    <div class="abs forest" role="img" aria-label="Misty black and white forest of tall tree trunks"></div>
    <p class="abs cover-intro">we can help you to</p>
    <h1 class="abs cover-title">Make Change Happen</h1>
    <p class="abs cover-pillars">strategy | people | technology</p>
    <div class="abs cover-badge">
      <div class="brand"><i></i><span>Kestrel<br>Advisory</span></div>
    </div>
  </section>

  <!-- Page 3 -->
  <section class="page p3">
    <div class="abs p3-wash"></div>
    <div class="abs p3-blue"></div>
    <h2 class="abs p3-title">Why Kestrel Advisory?</h2>

    <div class="abs reason" style="top:65px"><h3>Success</h3><p>We will deliver reliable results for you, as our services record shows. In the past few years, we have helped a numbers of organizations with a less than 2% rejection rate.</p></div>
    <div class="abs reason" style="top:118px"><h3>Targeting</h3><p>We understand the importance of targeting the right people and community, the right way. We will work with you to understand the importance of communication and how you can focus the right individual at a good time.</p></div>
    <div class="abs reason" style="top:171px"><h3>Superior Workforce</h3><p>Our dedicated training professionals have all been rigorously screened and training to perform at their peak level. They know that they represent our company at all times and understand the importance of enhancing your image.</p></div>
    <div class="abs reason" style="top:224px"><h3>Flexible Multichannel Abilities</h3><p>Our wide capabilities give an extensive reach and the ability to create exactly the right program and deliver it where it will get the best results.</p></div>
    <div class="abs reason" style="top:269px"><h3>Cost Effectiveness</h3><p>Kestrel Advisory will train your staff by offering very affordable value-added projects</p></div>

    <div class="abs photo" style="left:272px;top:64px" role="img" aria-label="Business team standing together in an office"></div>
    <div class="abs photo" style="left:393px;top:64px" role="img" aria-label="Smiling businesswoman with colleagues behind"></div>
    <div class="abs photo" style="left:272px;top:142px" role="img" aria-label="Executive seated at a meeting table"></div>
    <div class="abs photo" style="left:393px;top:142px" role="img" aria-label="Businesswoman in front of a working team"></div>
    <div class="abs photo" style="left:272px;top:220px" role="img" aria-label="Colleagues applauding in a seminar"></div>
    <div class="abs photo" style="left:393px;top:220px" role="img" aria-label="Confident businesswoman in a bright office"></div>

    <div class="abs footer" style="top:336px">
      <span class="pillars">strategy | people | technology</span>
      <span class="num">3</span>
      <span class="brand"><i></i>Kestrel Advisory</span>
    </div>
  </section>

  <!-- Page 1 -->
  <section class="page p1">
    <div class="abs toc">
      <h2 class="abs toc-title">Table of Contents</h2>
      <div class="toc-row main" style="top:39px"><span>Who we are?</span><span>2</span></div>
      <div class="toc-row sub" style="top:54px"><span>Executive Summary</span><span>2</span></div>
      <div class="toc-row sub" style="top:64px"><span>Vision</span><span>2</span></div>
      <div class="toc-row sub" style="top:73px"><span>Mission</span><span>2</span></div>
      <div class="toc-row sub" style="top:83px"><span>Values</span><span>2</span></div>
      <div class="toc-row main" style="top:94px"><span>Why Kestrel Advisory?</span><span>3</span></div>
      <div class="toc-row main" style="top:114px"><span>What we do?</span><span>4</span></div>
      <div class="toc-row sub" style="top:129px"><span>HR &amp; OD Consultation</span><span>4</span></div>
      <div class="toc-row sub" style="top:139px"><span>Professional Training</span><span>4</span></div>
      <div class="toc-row sub" style="top:148px"><span>Talent Assessment</span><span>5</span></div>
      <div class="toc-row sub" style="top:158px"><span>HR Solutions</span><span>5</span></div>
      <div class="toc-row main" style="top:168px"><span>Partnership</span><span>6</span></div>
      <div class="toc-row sub" style="top:186px"><span>(PMA) Pathway Management Associates, Inc.</span><span>6</span></div>
      <div class="toc-row sub" style="top:195px"><span>Harlow Pennington</span><span>6</span></div>
      <div class="toc-row sub" style="top:205px"><span>novatalents</span><span>6</span></div>
      <div class="toc-row sub" style="top:215px"><span>Verano Consulting</span><span>6</span></div>
      <div class="toc-row main" style="top:226px"><span>Our Team</span><span>7</span></div>
      <div class="toc-row sub" style="top:243px"><span>Tarek Al Mansouri Consulting Manager</span><span>7</span></div>
      <div class="toc-row sub" style="top:254px"><span>Yousef Darwish Assoc. Consultant</span><span>7</span></div>
      <div class="toc-row sub" style="top:265px"><span>Faisal Al-Nouri Projects Manager</span><span>8</span></div>
      <div class="toc-row sub" style="top:276px"><span>Karim Benali Assoc. Consultant</span><span>8</span></div>
      <div class="toc-row main" style="top:287px"><span>Certifications</span><span>9</span></div>
      <div class="toc-row main" style="top:304px"><span>Our Clients</span><span>10</span></div>
      <div class="toc-row main" style="top:319px"><span>Contact us</span><span>11</span></div>
    </div>
    <div class="abs p1-brand"><span class="brand"><i></i>Kestrel Advisory</span></div>
    <div class="abs p1-rule"></div>
  </section>

  <!-- Page 2 -->
  <section class="page p2">
    <div class="abs p2-band"></div>
    <h2 class="abs p2-title">Who We Are?</h2>

    <div class="abs" style="left:23px;top:53px;width:242px">
      <h3 class="h">Executive Summary</h3>
      <p class="copy" style="margin-top:3px">Kestrel Advisory is a professional HR &amp; OD Organization, which is specialized in Talent and Organizational Development, Career Coaching, Leadership Assessment and Development, Total Reward, HR Technology &amp; providing a wide range of outsourcing payroll and recruitment services with a vision to be the leading HR outsourcing company in the Middle East. Kestrel Advisory is a local house of HR &amp; OD expertise with global experience, driven by one thought, to raise the bar of local HR practices and knowledge. Kestrel Advisory has developed partnerships with various companies and organizations, among those novatalents will be the strategic partner to provide HR outsourcing services through their platforms.</p>
      <h3 class="h" style="margin-top:8px">Vision</h3>
      <p class="copy" style="margin-top:3px">"To become the leading HR outsourcing company in the Middle East and stand known of quality services."</p>
    </div>

    <div class="abs" style="left:284px;top:53px;width:228px">
      <h3 class="h">Mission</h3>
      <p class="copy" style="margin-top:3px;margin-bottom:5px">We have a multi-layered mission statement catering for the needs of our customers in addition to increasing the value of our services and upgrading our standing among our competitors. Our missions are:</p>
      <ul class="mission-list">
        <li>To provide convenient HR solutions to SMEs so they can focus on the core of their business.</li>
        <li>To play our role in economic development of Saudi Arabia and other Middle East countries.</li>
        <li>To develop a professional relationship with our valued clientele and investors.</li>
        <li>To bring innovation in HR services through technology.</li>
      </ul>
    </div>

    <div class="abs values">
      <div class="values-head"><span>Values</span><span></span></div>
      <div class="values-row"><span class="k"><svg viewBox="0 0 10 10"><circle cx="5" cy="5" r="5" fill="#fff"/><path d="M2.6 5.2l1.7 1.7 3.2-3.6" stroke="#2d6fb0" stroke-width="1.5" fill="none"/></svg>INTEGRITY:</span><span class="v">Kestrel Advisory will ensure integrity within employees and with clients, investors and strategic partners.</span></div>
      <div class="values-row"><span class="k"><svg viewBox="0 0 10 10"><circle cx="5" cy="5" r="5" fill="#fff"/><path d="M2.6 5.2l1.7 1.7 3.2-3.6" stroke="#2d6fb0" stroke-width="1.5" fill="none"/></svg>WORKPLACE ENTERTAINMENT:</span><span class="v">Kestrel Advisory will provide enjoyment of all employees at the workplace to promote work as a passion instead of a profession.</span></div>
      <div class="values-row"><span class="k"><svg viewBox="0 0 10 10"><circle cx="5" cy="5" r="5" fill="#fff"/><path d="M2.6 5.2l1.7 1.7 3.2-3.6" stroke="#2d6fb0" stroke-width="1.5" fill="none"/></svg>ACCOUNTABILITY:</span><span class="v">In Kestrel Advisory, from MD to staff everyone will be accountable for their actions and decision.</span></div>
      <div class="values-row"><span class="k"><svg viewBox="0 0 10 10"><circle cx="5" cy="5" r="5" fill="#fff"/><path d="M2.6 5.2l1.7 1.7 3.2-3.6" stroke="#2d6fb0" stroke-width="1.5" fill="none"/></svg>PURSUIT OF EXCELLENCE:</span><span class="v">Each employee and stakeholder will strive for excellence in his role and professional activities.</span></div>
      <div class="values-row"><span class="k"><svg viewBox="0 0 10 10"><circle cx="5" cy="5" r="5" fill="#fff"/><path d="M2.6 5.2l1.7 1.7 3.2-3.6" stroke="#2d6fb0" stroke-width="1.5" fill="none"/></svg>QUALITY CONTROL:</span><span class="v">Kestrel Advisory will implement strict quality control to improve the standard of its services continuously.</span></div>
      <div class="values-row"><span class="k"><svg viewBox="0 0 10 10"><circle cx="5" cy="5" r="5" fill="#fff"/><path d="M2.6 5.2l1.7 1.7 3.2-3.6" stroke="#2d6fb0" stroke-width="1.5" fill="none"/></svg>AFFORDABILITY:</span><span class="v">Services of Kestrel Advisory will be affordable to meet the demands of local companies.</span></div>
    </div>

    <div class="abs footer" style="top:337px">
      <span class="pillars">strategy | people | technology</span>
      <span class="num">2</span>
      <span class="brand"><i></i>Kestrel Advisory</span>
    </div>
  </section>

</div>
</body>
</html>
```